Corporate Brightfen business cards to be handed to investor, bankers etc. Needs to have a young feel

I need business cards designed for a technology company that provides uber-like rapid response on the security industry. I would like it simple but very cool and tasteful. See attached documents for artwork and colours to be used. Cut sheet describes business model. Card stock should be thicker than normal. I would like the one side to be just the art and the other to have the contact info with maybe the pin somewhere.

Target Market(s)

Investors

Industry/Entity Type

Business

Contact Information for Business Card

Would like the logo attached on one side with name address and other info on the other side.

Font styles to use
Other font styles liked:
• See existing logo

Colors
6b449b
886aae
e4daeb
ffffff

Requirements
Must have
• Name: Dorian Felkatsis
• Address: 47 Larkfield Avenue, Toronto, On, M6K2B7
• Tel: 416-7291846
• Email: rolo@brightfen.io
Nice to have
• See logo colours

```html
<!DOCTYPE html>
<html lang="en">
<head>
<meta charset="utf-8">
<title>Brightfen business cards</title>
<link rel="stylesheet" href="https://fonts.googleapis.com/css2?family=Quicksand:wght@500&display=swap">
<style>
  :root {
    --stage: #2e2e30;
    --card: #ffffff;
    --ink: #1a1a1a;
    --brand-deep: #6b449b;
    --brand-mist: #e4daeb;
  }
  * { margin: 0; padding: 0; box-sizing: border-box; }
  html, body {
    width: 1200px;
    height: 880px;
    overflow: hidden;
    background: var(--stage);
  }
  .canvas {
    position: relative;
    width: 1200px;
    height: 880px;
    font-family: "Quicksand", sans-serif;
    font-weight: 500;
    color: var(--ink);
  }
  .card {
    position: absolute;
    width: 600px;
    height: 343px;
    background: var(--card);
    border-radius: 22px;
    box-shadow: 0 14px 30px rgba(0, 0, 0, 0.45);
    display: flex;
    flex-direction: column;
    align-items: center;
    justify-content: center;
  }
  .card--front { left: 90px; top: 90px; }
  .card--back  { left: 510px; top: 447px; }

  .company-name {
    font-weight: 500;
    font-size: 64px;
    line-height: 1;
    letter-spacing: 1px;
    color: var(--ink);
  }
  .card--back .company-name { font-size: 56px; }

  .holder {
    margin-top: 28px;
    font-size: 21px;
    letter-spacing: 0.5px;
  }
  .contact {
    margin-top: 16px;
    list-style: none;
    text-align: center;
    font-size: 15px;
    line-height: 1.6;
    letter-spacing: 0.3px;
  }
</style>
</head>
<body>
  <main class="canvas">
    <section class="card card--front" aria-label="Card front">
      <p class="company-name">Brightfen</p>
    </section>

    <section class="card card--back" aria-label="Card back">
      <p class="company-name">Brightfen</p>
      <p class="holder">Dorian Felkatsis</p>
      <ul class="contact">
        <li>416-7291846</li>
        <li>rolo@brightfen.io</li>
        <li>47 Larkfield Avenue, Toronto, On, M6K2B7</li>
      </ul>
    </section>
  </main>
</body>
</html>
```